Design a (20.4 x 10.14) Banner that says - Keep Hope Rising From Harvest Crown TV Family

We want a design (20.4 x 10.14) with the words 'Keep Hope Rising' as the main text and 'From Harvest Crown TV Family' underneath. For 'Harvest Crown TV', we'd like you to use the logo which can be found in the image attached.

The image attached is just an example but please let your creative juices flow!

Target Market(s)

Christian

Industry/Entity Type

Christian

Requirements
Must have
• Must have the words 'Keep Hope Rising' and 'From Harvest Crown TV Family'.

```html
<!DOCTYPE html>
<html lang="en">
<head>
<meta charset="utf-8">
<title>Keep Hope Rising – Harvest Crown TV Family</title>
<link rel="stylesheet" href="https://fonts.googleapis.com/css2?family=Kaushan+Script&family=Orbitron:wght@900&family=Libre+Baskerville:wght@400;700&display=swap">
<style>
  :root {
    --violet-deep: #4a1fe0;
    --violet: #7d1fe6;
    --magenta: #d01fd6;
    --band-light: #a23cf0;
    --band-soft: #b84ef2;
    --ink: #0d0d0d;
    --white: #ffffff;
    --brand-navy: #34288a;
  }
  html, body {
    margin: 0;
    padding: 0;
    overflow: hidden;
    background: #ffffff;
  }
  .banner {
    position: relative;
    width: 1200px;
    height: 596px;
    overflow: hidden;
  }
  .banner-art {
    position: absolute;
    inset: 0;
    display: block;
  }
  .headline-script {
    font-family: "Kaushan Script", cursive;
    fill: var(--ink);
  }
  .headline-block {
    font-family: "Orbitron", sans-serif;
    font-weight: 900;
    fill: var(--ink);
  }
  .sign-off {
    position: absolute;
    left: 20px;
    top: 520px;
    margin: 0;
    font-family: "Libre Baskerville", serif;
    font-size: 27px;
    color: var(--white);
    letter-spacing: 0.5px;
  }
  .brand-name {
    position: absolute;
    right: 40px;
    top: 14px;
    margin: 0;
    font-family: "Libre Baskerville", serif;
    font-weight: 700;
    font-size: 30px;
    color: var(--brand-navy);
  }
  .contact {
    position: absolute;
    top: 520px;
    display: flex;
    align-items: center;
    gap: 8px;
    font-family: "Libre Baskerville", serif;
    font-size: 17px;
    color: var(--white);
  }
  .contact-web { left: 712px; }
  .contact-social { left: 962px; }
  .contact-icon {
    width: 32px;
    height: 32px;
    flex: none;
  }
  .social-dot {
    width: 32px;
    height: 32px;
    border-radius: 50%;
    background: var(--white);
    flex: none;
  }
</style>
</head>
<body>
<div class="banner">
  <svg class="banner-art" viewBox="0 0 1200 596" width="1200" height="596" aria-hidden="false">
    <defs>
      <linearGradient id="bgGradient" x1="0" y1="0" x2="1" y2="1">
        <stop offset="0" stop-color="var(--violet-deep)"/>
        <stop offset="0.5" stop-color="var(--violet)"/>
        <stop offset="1" stop-color="var(--magenta)"/>
      </linearGradient>
      <linearGradient id="skyGradient" x1="0" y1="1" x2="1" y2="0">
        <stop offset="0" stop-color="#1f3c9c"/>
        <stop offset="0.35" stop-color="#8a3f9c"/>
        <stop offset="0.55" stop-color="#e0449a"/>
        <stop offset="0.8" stop-color="#e9c6df"/>
        <stop offset="1" stop-color="#3f7fd0"/>
      </linearGradient>
    </defs>

    <rect class="backdrop" width="1200" height="596" fill="url(#bgGradient)"/>
    <path class="band band-outer" d="M0,250 C160,90 380,20 600,0 L1200,0 L1200,420 C980,500 760,560 520,596 L0,596 Z" fill="var(--band-light)" opacity="0.45"/>
    <path class="band band-inner" d="M0,280 C160,110 370,30 580,0 L1150,0 C1170,140 1185,260 1200,360 C990,470 780,540 540,596 L0,596 Z" fill="var(--band-soft)" opacity="0.45"/>

    <path class="sky-photo" role="img" aria-label="Photo of a cloudy pink and blue sky with red and pink heart balloons floating upward"
          d="M0,300 C150,130 350,35 565,0 L1110,0 C1140,120 1165,220 1195,300 C1000,420 780,500 540,572 C360,580 180,585 0,585 Z"
          fill="url(#skyGradient)"/>

    <text class="headline-script" x="330" y="172" font-size="92">Keep</text>
    <text class="headline-block" x="205" y="334" font-size="150" textLength="755" lengthAdjust="spacingAndGlyphs">HOPE</text>
    <text class="headline-script" x="690" y="460" font-size="86">Rising</text>
  </svg>

  <p class="brand-name">harvestcrown.tv</p>

  <p class="sign-off">From Harvest Crown TV Family</p>

  <div class="contact contact-web">
    <svg class="contact-icon" viewBox="0 0 32 32" aria-hidden="true">
      <g fill="none" stroke="#ffffff" stroke-width="2">
        <circle cx="16" cy="16" r="14"/>
        <ellipse cx="16" cy="16" rx="6" ry="14"/>
        <line x1="2" y1="16" x2="30" y2="16"/>
        <path d="M5,9 H27 M5,23 H27"/>
      </g>
    </svg>
    <span>www.harvestcrown.tv</span>
  </div>

  <div class="contact contact-social">
    <span class="social-dot" aria-hidden="true"></span>
    <span>hcministries</span>
  </div>
</div>
</body>
</html>
```